Harborline Energy - needs a business card

Harborline Energy is a U.S. based diesel sourcing and distribution company that supports American oil & gas fields through providing quality product and consistent services.

Target Market(s)

Oil and Gas

Contact Information for Business Card

The background of the card must be white to ensure the logo pops.

Font styles to use
Serif
Sans Serif

Colors

Designer to choose colors to be used in the design.

Requirements
Must have
• Front of Card: Tag line: Harborline Energy, Powering America's Oil & Gas fields.
• Not sure if you guys do this part but just in case...
• Dale Menschow
• Owner/CEO
• C:555.318.4076
• E:Dmenschow@harborlineenergy.example
• W:Harborlineenergy.example
• Locations: Servicing the Powder River, DJ basin and Bakken formations.
• Back of Card: " Frac fueling is what we do. We understand how important diesel fuel is to your operation, which is why our main service line is Frac fueling. We assure our supply and stand by our service"

```html
<!DOCTYPE html>
<html lang="en">
<head>
<meta charset="UTF-8">
<title>Harborline Energy – Business Card</title>
<link href="https://fonts.googleapis.com/css2?family=Open+Sans:ital,wght@0,400;0,600;0,800;1,400&display=swap" rel="stylesheet">
<style>
  :root {
    --navy: #1b2f63;
    --red: #b3202a;
    --ink: #2a2a2a;
    --card: #ffffff;
    --backdrop: #e9e6e1;
  }
  * { margin: 0; padding: 0; box-sizing: border-box; }
  html, body { width: 1200px; height: 900px; overflow: hidden; }
  body {
    background: var(--backdrop);
    font-family: "Open Sans", Arial, sans-serif;
    position: relative;
  }
  .card {
    position: absolute;
    left: 300px;
    width: 600px;
    height: 343px;
    background: var(--card);
    box-shadow: 0 6px 18px rgba(0,0,0,0.18);
    overflow: hidden;
  }
  .card--back { top: 70px; }
  .card--front { top: 470px; }

  .wordmark {
    position: absolute;
    display: flex;
    align-items: center;
    gap: 10px;
    color: var(--navy);
    font-weight: 800;
    font-size: 26px;
    letter-spacing: 0.5px;
    white-space: nowrap;
  }
  .wordmark__dot {
    width: 34px; height: 34px;
    border-radius: 50%;
    background: var(--navy);
    flex: none;
  }
  .card--back .wordmark { left: 50%; top: 105px; transform: translateX(-50%); }
  .card--front .wordmark { left: 36px; top: 50px; font-size: 22px; }

  .service-note {
    position: absolute;
    left: 60px; right: 60px; top: 190px;
    text-align: center;
    color: var(--navy);
    font-style: italic;
    font-size: 12px;
    line-height: 1.6;
  }

  .divider {
    position: absolute;
    left: 30px; right: 0; top: 118px;
    height: 1.5px;
    background: var(--navy);
  }
  .contact {
    position: absolute;
    left: 30px; top: 132px;
    font-size: 13px;
    line-height: 1.45;
    color: var(--ink);
    list-style: none;
  }
  .contact__label { color: var(--navy); font-weight: 800; }

  .person {
    position: absolute;
    right: 30px; top: 176px;
    text-align: right;
  }
  .person__name { color: var(--red); font-weight: 800; font-size: 22px; line-height: 1.1; }
  .person__role { color: var(--navy); font-size: 11px; font-weight: 600; }

  .locations {
    position: absolute;
    right: 30px; top: 222px;
    width: 290px;
    text-align: right;
    font-size: 12.5px;
    line-height: 1.35;
    color: var(--ink);
  }
  .locations__label { color: var(--navy); font-weight: 800; }

  .bands { position: absolute; left: 0; bottom: 0; }
  .tagline {
    position: absolute;
    left: 24px; top: 281px;
    color: #fff;
    font-size: 12.5px;
    line-height: 16px;
    white-space: nowrap;
  }
</style>
</head>
<body>

<section class="card card--back" aria-label="Back of card">
  <div class="wordmark"><span class="wordmark__dot"></span>Harborline Energy</div>
  <p class="service-note">Frac fueling is what we do. We understand how important diesel fuel is to your operation, which is why our main service line is Frac fueling. We assure our supply and stand by our service</p>
</section>

<section class="card card--front" aria-label="Front of card">
  <div class="wordmark"><span class="wordmark__dot"></span>Harborline Energy</div>
  <div class="divider"></div>
  <ul class="contact">
    <li><span class="contact__label">Cell:</span> 555.318.4076</li>
    <li><span class="contact__label">Email:</span> Dmenschow@harborlineenergy.example</li>
    <li><span class="contact__label">Web:</span> Harborlineenergy.example</li>
  </ul>
  <div class="person">
    <div class="person__name">Dale Menschow</div>
    <div class="person__role">Owner/CEO</div>
  </div>
  <p class="locations"><span class="locations__label">Locations:</span> Servicing the Powder River, DJ basin and Bakken formations</p>
  <svg class="bands" width="600" height="100" viewBox="0 0 600 100" aria-hidden="true">
    <polygon points="0,30 385,30 375,62 0,62" fill="var(--navy)"/>
    <polygon points="378,62 600,62 600,86 370,86" fill="var(--red)"/>
  </svg>
  <p class="tagline">Harborline Energy, Powering America's Oil &amp; Gas fields.</p>
</section>

</body>
</html>
```